I need a business card.

I need a simple, minimalist, business card. I think the coolest business card I have ever seen is Marty Vexler's from Brimstone Heist... it is just a little creepy for the real world.
I am a photographer and I need a card that I can give to brides or potential portrait customers that is simple and classy.
My name is Gil Anstrade. My website is www.gilanstrade-example.com
Please design my card.
I think it could be as simple as my name, phone # and website... where the rest of my contact could be found... or maybe my email and no website... I am open to ideas. I imagined the card on thick card stock with a black background...

```html
<!DOCTYPE html>
<html lang="en">
<head>
<meta charset="utf-8">
<title>Gil Anstrade — Photographer Business Card</title>
<link rel="stylesheet" href="https://fonts.googleapis.com/css2?family=Bodoni+Moda:ital,wght@0,500;0,700;1,400&family=Didact+Gothic&display=swap">
<style>
  :root {
    --stage: #f3f3f3;
    --card: #262626;
    --pattern-a: #2d2d2d;
    --pattern-b: #242424;
    --orange: #f7941d;
    --white: #ffffff;
    --label-bg: #2a2a2a;
    --soft-white: #e6e6e6;
  }
  * { margin: 0; padding: 0; box-sizing: border-box; }
  html, body {
    width: 1200px;
    height: 837px;
    overflow: hidden;
    background: var(--stage);
  }
  .stage {
    position: relative;
    width: 1200px;
    height: 837px;
  }
  .card {
    position: absolute;
    top: 131px;
    width: 340px;
    height: 578px;
    background: var(--card);
    overflow: hidden;
  }
  .card--front { left: 229px; }
  .card--back { left: 620px; }

  /* Front */
  .front-texture {
    position: absolute;
    inset: 0;
    background: radial-gradient(circle at 50% 45%, var(--pattern-a), var(--pattern-b));
  }
  .accent-band {
    position: absolute;
    left: 202px;
    top: 0;
    width: 87px;
    height: 100%;
    background: var(--orange);
  }
  .name-plate {
    position: absolute;
    left: 195px;
    top: 351px;
    width: 94px;
    height: 57px;
    background: var(--label-bg);
    text-align: center;
    padding-top: 6px;
  }
  .name-plate__name {
    display: block;
    font-family: "Bodoni Moda", serif;
    font-weight: 700;
    font-size: 17px;
    letter-spacing: -0.3px;
    color: var(--orange);
    line-height: 1.1;
  }
  .name-plate__role {
    display: block;
    font-family: "Bodoni Moda", serif;
    font-style: italic;
    font-size: 12.5px;
    color: var(--soft-white);
    line-height: 1.3;
  }

  /* Back */
  .stripe {
    position: absolute;
    top: 0;
    height: 100%;
    display: flex;
    flex-direction: column;
    align-items: center;
  }
  .stripe--call { left: 240px; width: 20px; }
  .stripe--web { left: 262px; width: 20px; }
  .stripe__bar { width: 8px; background: var(--orange); }
  .stripe--web .stripe__bar { width: 14px; background: var(--white); }
  .stripe__bar--top-call { height: 52px; }
  .stripe__bar--top-web { height: 146px; }
  .stripe__bar--fill { flex: 1; }
  .stripe__text {
    writing-mode: vertical-rl;
    transform: rotate(180deg);
    white-space: nowrap;
    margin: 7px 0;
  }
  .call-line {
    font-family: "Didact Gothic", sans-serif;
    font-size: 18px;
    letter-spacing: 1.6px;
    color: var(--orange);
  }
  .call-line__label { font-size: 13px; letter-spacing: 1px; margin-right: 4px; }
  .web-line {
    font-family: "Bodoni Moda", serif;
    font-weight: 700;
    font-size: 14.5px;
    color: var(--white);
  }
</style>
</head>
<body>
<main class="stage">
  <section class="card card--front" aria-label="Card front">
    <div class="front-texture" role="img" aria-label="Dark repeating circular lace pattern"></div>
    <div class="accent-band"></div>
    <div class="name-plate">
      <span class="name-plate__name">gilanstrade</span>
      <span class="name-plate__role">photographer</span>
    </div>
  </section>

  <section class="card card--back" aria-label="Card back">
    <div class="stripe stripe--call">
      <div class="stripe__bar stripe__bar--top-call"></div>
      <p class="stripe__text call-line"><span class="call-line__label">call</span>0198765432</p>
      <div class="stripe__bar stripe__bar--fill"></div>
    </div>
    <div class="stripe stripe--web">
      <div class="stripe__bar stripe__bar--top-web"></div>
      <p class="stripe__text web-line">www.gilanstrade-example.com</p>
      <div class="stripe__bar stripe__bar--fill"></div>
    </div>
  </section>
</main>
</body>
</html>
```